Accounting services

Looking for a Business card & Logo design

company name - LUMEN ACCOUNTING & TAXATION SOLUTIONS

name - Corwin Pell

position - Accountant / Business Consultant

email - "undecided"

Tel : (868) 512-4873 / (868) 587-2196

**PUT THESE TO THE BACK**
Accounting - VAT * INCOME/CORP TAX * RETURNS

REGISTRATION - VAT * NIS * Company Registration/Business Plan

Industry/Entity Type

Business

```html
<!DOCTYPE html>
<html lang="en">
<head>
<meta charset="utf-8">
<title>Lumen Accounting &amp; Taxation Solutions – Business Cards</title>
<link rel="stylesheet" href="https://fonts.googleapis.com/css2?family=Libre+Baskerville:wght@400;700&display=swap">
<style>
  :root{
    --backdrop:#ebe8e3;
    --paper:#ffffff;
    --grey-light:#9d9e9e;
    --grey-dark:#6f6f6e;
    --red:#e1242b;
    --ink:#3a3a3a;
    --text-light:#ffffff;
    --shadow:rgba(0,0,0,.22);
  }
  *{box-sizing:border-box;margin:0;padding:0}
  html,body{width:1200px;height:780px;overflow:hidden}
  body{background:var(--backdrop);font-family:"Libre Baskerville",Georgia,serif;position:relative}

  .card{position:absolute;width:550px;height:330px;overflow:hidden;box-shadow:0 2px 6px var(--shadow)}
  .card--front-light{left:45px;top:45px;background:var(--grey-light)}
  .card--front-dark{left:615px;top:45px;background:var(--grey-dark)}
  .card--back-light{left:45px;top:418px;background:var(--grey-light)}
  .card--back-dark{left:615px;top:418px;background:var(--grey-dark)}

  .panel{position:absolute;left:0;top:0;width:196px;height:100%;background:var(--paper)}
  .divider{position:absolute;top:0;left:196px;width:4px;height:100%;background:var(--red)}

  .brand{position:absolute;left:23px;top:0;width:150px;height:100%;display:flex;align-items:center;justify-content:center;
    text-align:center;color:var(--ink);font-weight:700;font-size:14px;line-height:21px;letter-spacing:.5px}

  .contact{position:absolute;left:235px;top:48px;color:var(--text-light)}
  .contact__name{font-size:19px;font-weight:700;margin-bottom:9px}
  .contact__title{font-size:16px;font-weight:400;margin-bottom:22px}
  .contact__list{list-style:none;font-size:16px;line-height:25px}
  .contact__row{display:flex;align-items:center;gap:8px}
  .contact__row--web{font-weight:700;margin-top:8px}
  .icon{width:16px;height:16px;flex:none;fill:none;stroke:var(--red);stroke-width:1.6}
  .icon--solid{fill:var(--red);stroke:none}

  .services{position:absolute;left:225px;top:82px;color:var(--text-light);font-weight:700;font-size:15px;line-height:21px}
  .services__heading{color:var(--red);font-size:16px;line-height:21px}
  .card--back-dark .services__heading{color:var(--text-light)}
  .services__group + .services__heading{margin-top:14px}
  .services__group{list-style:none}
  .services__group li{position:relative;padding-left:15px}
  .services__group li::before{content:"•";position:absolute;left:0;color:var(--red)}
</style>
</head>
<body>

<section class="card card--front-light">
  <div class="panel"></div>
  <div class="divider"></div>
  <p class="brand">LUMEN ACCOUNTING &amp; TAXATION SOLUTIONS</p>
  <div class="contact">
    <h1 class="contact__name">Corwin Pell</h1>
    <p class="contact__title">Accountant/Business Consultant</p>
    <ul class="contact__list">
      <li class="contact__row">
        <svg class="icon icon--solid" viewBox="0 0 16 16"><path d="M4 1l3 3-1.6 1.8c.8 1.9 2.1 3.3 4 4.1L11.2 8.3l3 3-1.8 2.5C7 13.3 2.6 8.9 1.6 3z"/></svg>
        <span>(868) 512-4873<br>(868) 587-2196</span>
      </li>
      <li class="contact__row">
        <svg class="icon" viewBox="0 0 16 16"><rect x="1.5" y="3.5" width="13" height="9"/><path d="M1.5 3.5l6.5 5 6.5-5"/></svg>
        <span>corwin@lumensolutions.com</span>
      </li>
      <li class="contact__row contact__row--web">
        <svg class="icon" viewBox="0 0 16 16"><circle cx="8" cy="8" r="6.5"/><ellipse cx="8" cy="8" rx="3" ry="6.5"/><path d="M1.5 8h13M2.5 5h11M2.5 11h11"/></svg>
        <span>www.lumensolutions.com</span>
      </li>
    </ul>
  </div>
</section>

<section class="card card--front-dark">
  <div class="panel"></div>
  <div class="divider"></div>
  <p class="brand">LUMEN ACCOUNTING &amp; TAXATION SOLUTIONS</p>
  <div class="contact">
    <h2 class="contact__name">Corwin Pell</h2>
    <p class="contact__title">Accountant/Business Consultant</p>
    <ul class="contact__list">
      <li class="contact__row">
        <svg class="icon icon--solid" viewBox="0 0 16 16"><path d="M4 1l3 3-1.6 1.8c.8 1.9 2.1 3.3 4 4.1L11.2 8.3l3 3-1.8 2.5C7 13.3 2.6 8.9 1.6 3z"/></svg>
        <span>(868) 512-4873<br>(868) 587-2196</span>
      </li>
      <li class="contact__row">
        <svg class="icon" viewBox="0 0 16 16"><rect x="1.5" y="3.5" width="13" height="9"/><path d="M1.5 3.5l6.5 5 6.5-5"/></svg>
        <span>corwin@lumensolutions.com</span>
      </li>
      <li class="contact__row contact__row--web">
        <svg class="icon" viewBox="0 0 16 16"><circle cx="8" cy="8" r="6.5"/><ellipse cx="8" cy="8" rx="3" ry="6.5"/><path d="M1.5 8h13M2.5 5h11M2.5 11h11"/></svg>
        <span>www.lumensolutions.com</span>
      </li>
    </ul>
  </div>
</section>

<section class="card card--back-light">
  <div class="panel"></div>
  <div class="divider"></div>
  <p class="brand">LUMEN ACCOUNTING &amp; TAXATION SOLUTIONS</p>
  <div class="services">
    <h3 class="services__heading">ACCOUNTING</h3>
    <ul class="services__group">
      <li>VAT</li>
      <li>INCOME/CORP TAX</li>
      <li>RETURNS</li>
    </ul>
    <h3 class="services__heading">REGISTRATION</h3>
    <ul class="services__group">
      <li>VAT</li>
      <li>NIS</li>
      <li>COMPANY REGISTRATION /<br>BUSINESS PLAN</li>
    </ul>
  </div>
</section>

<section class="card card--back-dark">
  <div class="panel"></div>
  <div class="divider"></div>
  <p class="brand">LUMEN ACCOUNTING &amp; TAXATION SOLUTIONS</p>
  <div class="services">
    <h3 class="services__heading">ACCOUNTING</h3>
    <ul class="services__group">
      <li>VAT</li>
      <li>INCOME/CORP TAX</li>
      <li>RETURNS</li>
    </ul>
    <h3 class="services__heading">REGISTRATION</h3>
    <ul class="services__group">
      <li>VAT</li>
      <li>NIS</li>
      <li>COMPANY REGISTRATION /<br>BUSINESS PLAN</li>
    </ul>
  </div>
</section>

</body>
</html>
```